Business cards for start-up accounting firm

I'm looking for a double sided business card ready for upload into Lumo print or similar print providers with no modification required by me.
I'm looking for something simple as i think cards that are too 'busy' actually detract from the message. I have some thoughts but more than happy to see what comes up. The logo i have came out of left field and i love it the moment i saw it!

My thoughts:

Side 1: Just the logo, perhaps on a dark grey or charcoal background to make the logo colours stand out?

Side 2: The call to action from me website 'Looking for a more relaxed, friendly and interactive relationship with your accountant?' with my contact information
Name: Gus Tarrow
Email: gus@ledgerowl.com.au
Website: www.ledgerowl.com.au
Phone: 1300 762 349

The call to action needs to be the first thing they see when they look at side 2. If it helps to know what we do and how we do it there is a draft website at www.ledgerowl.com.au

Like i said, happy to consider anything that comes up :)

Target Market(s)

i'm targeting small business owners who experience a lot of stress around finacial reporting and have had bad experiences with accountants in the past.

Industry/Entity Type

Accounting

Contact Information for Business Card

Contained in the Description

Font styles to use
Serif
Sans Serif
Other font styles liked:
• See logo files attached

Colors
474747

Requirements
Must have
• My logo, slogan and contact information

```html
<!DOCTYPE html>
<html lang="en">
<head>
<meta charset="utf-8">
<title>Ledger Owl – Business Cards</title>
<link href="https://fonts.googleapis.com/css2?family=Open+Sans:wght@400;600;700;800&display=swap" rel="stylesheet">
<style>
  :root {
    --backdrop: #2e2e2e;
    --card: #060606;
    --purple: #8d2d8a;
    --lilac: #b68ac2;
    --yellow: #f6d313;
    --white: #ffffff;
  }
  * { box-sizing: border-box; margin: 0; padding: 0; }
  html, body { width: 1200px; height: 900px; overflow: hidden; }
  body {
    background: var(--backdrop);
    font-family: "Open Sans", Arial, sans-serif;
    position: relative;
  }
  .card {
    position: absolute;
    width: 560px;
    height: 320px;
    background: var(--card);
    border-radius: 18px;
    overflow: hidden;
  }
  .card--front { left: 70px; top: 90px; }
  .card--back { left: 570px; top: 490px; }
  .card__bands { position: absolute; left: 0; top: 0; width: 100%; height: 100%; }

  .brand {
    position: absolute;
    display: flex;
    align-items: center;
    gap: 12px;
    font-weight: 800;
    color: var(--purple);
    letter-spacing: 1px;
    line-height: 1;
    text-transform: uppercase;
    white-space: nowrap;
  }
  .brand__dot { width: 0.5em; height: 0.5em; border-radius: 50%; background: var(--yellow); flex: none; }
  .card--front .brand { left: 110px; top: 120px; font-size: 50px; }
  .front__web {
    position: absolute; right: 40px; bottom: 36px;
    color: var(--white); font-size: 14px; font-weight: 600;
  }

  .card--back .brand { left: 30px; top: 34px; font-size: 32px; gap: 9px; }
  .back__cta {
    position: absolute; left: 30px; top: 100px; width: 330px;
    color: var(--white); font-size: 12.5px; font-weight: 600;
    text-transform: uppercase; line-height: 1.4;
  }
  .back__name {
    position: absolute; right: 34px; top: 118px;
    color: var(--white); font-size: 22px; font-weight: 700;
    text-transform: uppercase; line-height: 1.2;
  }
  .back__contacts {
    position: absolute; left: 30px; bottom: 26px;
    list-style: none; color: var(--white); font-size: 13.5px; font-weight: 600;
  }
  .back__contacts li { display: flex; align-items: center; gap: 10px; line-height: 1.4; }
  .back__contacts svg { width: 11px; height: 11px; flex: none; }
</style>
</head>
<body>

<section class="card card--front" aria-label="Card front">
  <svg class="card__bands" viewBox="0 0 560 320" aria-hidden="true">
    <polygon points="240,300 560,300 560,312 248,312" fill="var(--lilac)"/>
    <polygon points="0,290 236,290 256,320 0,320" fill="var(--yellow)"/>
  </svg>
  <div class="brand"><span class="brand__dot"></span>Ledger Owl</div>
  <p class="front__web">www.ledgerowl.com.au</p>
</section>

<section class="card card--back" aria-label="Card back">
  <svg class="card__bands" viewBox="0 0 560 320" aria-hidden="true">
    <polygon points="420,236 560,236 560,320 412,320" fill="var(--purple)"/>
    <polygon points="0,304 417,304 415,316 0,316" fill="var(--lilac)"/>
    <polyline points="30,226 380,153 530,153" fill="none" stroke="var(--yellow)" stroke-width="1.5"/>
  </svg>
  <div class="brand"><span class="brand__dot"></span>Ledger Owl</div>
  <p class="back__cta">Looking for a more relaxed friendly and interactive relationship with your accountant</p>
  <p class="back__name">Gus Tarrow</p>
  <ul class="back__contacts">
    <li>
      <svg viewBox="0 0 12 12"><path d="M2.5 1 L4.5 1 L5 3.5 L3.8 4.5 Q5 7 7.5 8.2 L8.5 7 L11 7.5 L11 9.5 Q10.5 11 9 11 Q1 10 1 2.5 Q1 1 2.5 1 Z" fill="var(--yellow)"/></svg>
      1300 762 349
    </li>
    <li>
      <svg viewBox="0 0 12 12"><rect x="0.8" y="2.3" width="10.4" height="7.4" fill="none" stroke="var(--yellow)" stroke-width="1.2"/><polyline points="1,2.6 6,6.6 11,2.6" fill="none" stroke="var(--yellow)" stroke-width="1.2"/></svg>
      gus@ledgerowl.com.au
    </li>
    <li>
      <svg viewBox="0 0 12 12"><circle cx="6" cy="6" r="5.2" fill="none" stroke="var(--yellow)" stroke-width="1.2"/><ellipse cx="6" cy="6" rx="2.2" ry="5.2" fill="none" stroke="var(--yellow)" stroke-width="1"/><line x1="0.8" y1="6" x2="11.2" y2="6" stroke="var(--yellow)" stroke-width="1"/></svg>
      www.ledgerowl.com.au
    </li>
  </ul>
</section>

</body>
</html>
```